Health & Beauty Company- Business Card Design

Two-sided business card design and logo design.

Company markets and sells otc treatments for the health and beauty industry. Marketing products to doctors, pharmacists and retail drug companies like tormundos, pqz and lumo fex.

Designs should be submitted as vector based PDFs. To keep your text in vector format, our printer recommends applications like Adobe Illustrator, Adobe InDesign and more recent versions of Adobe Photoshop.

Target Market(s)

Drug stores, doctors and pharmacists

Industry/Entity Type

Printer

Requirements
Must have
• Back side of business card should include company logo and our tagline: "Innovating the Health & Beauty Experience"

Company name acronym must be included: QTRM

```html
<!DOCTYPE html>
<html lang="en">
<head>
<meta charset="utf-8">
<title>QTRM Business Card Design</title>
<link href="https://fonts.googleapis.com/css2?family=Tenor+Sans&family=Tinos:wght@700&family=Arimo:wght@700&display=swap" rel="stylesheet">
<style>
  :root {
    --paper: #ffffff;
    --ink: #000000;
    --card-dark: #0d0d0d;
    --card-mid: #4a4a4a;
    --card-light: #a3a3a3;
    --mark-dark: #111111;
    --text-light: #ffffff;
    --text-soft: #f0f0f0;
  }
  html, body {
    margin: 0;
    padding: 0;
    width: 1200px;
    height: 495px;
    overflow: hidden;
    background: var(--paper);
  }
  .sheet {
    position: relative;
    width: 1200px;
    height: 495px;
  }
  .sheet-frame {
    position: absolute;
    left: 0;
    top: 0;
    width: 1051px;
    height: 480px;
    border: 4px solid var(--ink);
  }
  .card {
    position: absolute;
    top: 98px;
    width: 451px;
    height: 257px;
    border: 3px solid var(--ink);
    overflow: hidden;
  }
  .card--front {
    left: 56px;
    background: linear-gradient(to top right, var(--card-dark) 0%, var(--card-mid) 45%, var(--card-light) 100%);
  }
  .card--back {
    left: 546px;
    background: linear-gradient(to top right, var(--card-dark) 0%, var(--card-mid) 40%, var(--card-light) 100%);
  }
  .brand-name {
    position: absolute;
    margin: 0;
    font-family: "Tenor Sans", sans-serif;
    font-weight: 400;
    color: var(--mark-dark);
    line-height: 1;
  }
  .card--front .brand-name {
    left: 0;
    width: 100%;
    top: 72px;
    text-align: center;
    font-size: 74px;
    padding-left: 18px;
    box-sizing: border-box;
  }
  .tagline {
    position: absolute;
    margin: 0;
    font-family: "Arimo", sans-serif;
    font-weight: 700;
    color: var(--mark-dark);
    white-space: nowrap;
  }
  .card--front .tagline {
    left: 0;
    width: 100%;
    top: 155px;
    text-align: center;
    font-size: 14.6px;
    padding-left: 18px;
    box-sizing: border-box;
  }
  .card--back .brand-name {
    left: 56px;
    top: 20px;
    font-size: 28px;
  }
  .card--back .tagline {
    left: 8px;
    top: 52px;
    font-size: 7.8px;
  }
  .holder {
    position: absolute;
    left: 25px;
    top: 140px;
    margin: 0;
    font-family: "Tinos", serif;
    font-weight: 700;
    color: var(--text-light);
  }
  .holder-name {
    display: block;
    font-size: 28px;
    line-height: 1;
  }
  .holder-title {
    display: block;
    margin: 8px 0 0 17px;
    font-size: 15px;
    line-height: 1;
  }
  .contact {
    position: absolute;
    left: 286px;
    top: 48px;
    margin: 0;
    font-family: "Tinos", serif;
    font-weight: 700;
    font-size: 15px;
    line-height: 19px;
    color: var(--text-soft);
    font-style: normal;
  }
  .contact-group {
    margin: 0 0 18px 0;
  }
  .contact-group--phones {
    margin-bottom: 28px;
  }
  .contact-group:last-child {
    margin-bottom: 0;
  }
  .card-label {
    position: absolute;
    margin: 0;
    font-family: "Tinos", serif;
    font-weight: 700;
    font-size: 24px;
    color: var(--ink);
  }
  .card-label--front { left: 196px; top: 381px; }
  .card-label--back { left: 725px; top: 387px; }
</style>
</head>
<body>
<main class="sheet">
  <div class="sheet-frame"></div>

  <section class="card card--front" aria-label="Card front">
    <h1 class="brand-name">QTRM</h1>
    <p class="tagline">Elevating the Wellness &amp; Radiant Care Journey</p>
  </section>

  <section class="card card--back" aria-label="Card back">
    <p class="brand-name">QTRM</p>
    <p class="tagline">Elevating the Wellness &amp; Radiant Care Journey</p>

    <p class="holder">
      <span class="holder-name">Name xxxxx</span>
      <span class="holder-title">President &amp; CEO</span>
    </p>

    <address class="contact">
      <div class="contact-group">
        Company<br>
        Address xxxxxx<br>
        City,State Zip code
      </div>
      <div class="contact-group contact-group--phones">
        xxx.xxx.xxxx<br>
        xxx.xxx.xxxx&nbsp;&nbsp;FAX
      </div>
      <div class="contact-group">
        xxxx@xxxxxxxxx.com<br>
        xxxx.xxxxx Skype
      </div>
    </address>
  </section>

  <p class="card-label card-label--front">Card front</p>
  <p class="card-label card-label--back">Card Back</p>
</main>
</body>
</html>
```